Your Health, Your Time, Your Way: Personalized, Concierge Care Elevated to Modern Medicine

We need to incorporate an image of our new doctor (Dr. Malvina Okoruwe, MD) with our office logo ( Harborline Family Clinic) and dialogue that shows how simple it is to schedule a free consult and learn what our office has to offer patients. The colors should be consistent with our website- the CMYK codes will be attached for your use below. The font should be easy to read. The text should be clear, and convey value to the patient for chosing us over anyone else ( we offer primary care, preventive medicine, urgen care and functional medicine with 24 hour direct access to care with some of our strengths including focus on individualized care, cutting edge medicine, blended functional and traditional style. We aim to transform lives through patient centered innovative and individualized care plan. I have attached a "mock" image but the details ( office address, name, phone number are incorrect) The correct info is Harborline Family Clinic 4187 Wrenfield Ave Suite 214, Clearwater, FL 33759 and phone number (727)482-3095. A possible hook could read: welcoming new patients now- Your Health, Your Time, Your Way: Personalized Care Meets Modern Medicine
Updates

I did not realize that there was a tab with more information to fill for the designers to see, or for me to upload the basic information they need to create the design.

Target Market(s)

Patients over 18 years of age with interest in longevity, functional and traditional medicine; the postcards will be mailed to our CURRENT patients, and they are a reminder of what we do, new patient availability AND a request for them to refer friends or families

Industry/Entity Type

medical

Font styles to use
Sans Serif

Colors

Designer to choose colors to be used in the design.

Requirements
Must have
• simple reminder to current patients of what we offer, and a call to action for our patients to refer friends and family for same level of excellence;consistency with brand ( see business card and cmyx codes for colors);photo of new physician; logo Harborline Family Clinic, web site (https://harborlinefamilyclinic.net); Must clearly express accepting new patients; simple to call/email to schedule free consultation;; include our email (office@harborlinefamilyclinic.org), phone number (727)482-3095; our address 4187 Wrenfield Ave Suite 214, Clearwater, FL 33759
Nice to have
• photo of our new physician ( in blue jacket: Dr. Malvina Okoruwe, MD) should not take up too much space
Should not have
• clutter, or close text; full sentences( bulleted text preferred)

```html
<!DOCTYPE html>
<html lang="en">
<head>
<meta charset="utf-8">
<title>Harborline Family Clinic – Postcard</title>
<link href="https://fonts.googleapis.com/css2?family=Bebas+Neue&family=Poppins:ital,wght@0,400;0,500;0,600;0,700;0,800;1,400;1,500&display=swap" rel="stylesheet">
<style>
  :root{
    --navy:#0d3c86;
    --teal:#138b8a;
    --green:#3cc47c;
    --mint:#a4e6d6;
    --white:#ffffff;
    --ink:#0b2c6b;
    --silver-1:#f4f5f7;
    --silver-2:#9ea3aa;
    --stage:#f1f1f1;
  }
  *{margin:0;padding:0;box-sizing:border-box}
  html,body{width:1200px;height:479px;overflow:hidden;background:var(--stage)}
  body{position:relative;font-family:'Poppins',sans-serif;color:var(--white)}
  .card{position:absolute;top:87px;width:450px;height:305px;background:var(--white);overflow:hidden;box-shadow:0 4px 10px rgba(0,0,0,.25)}
  .card--front{left:138px}
  .card--back{left:612px}
  .shape{position:absolute;inset:0}
  .abs{position:absolute}

  /* front */
  .brand{left:14px;top:30px;width:62px;font-size:9px;line-height:11px;font-weight:500;color:var(--white)}
  .divider{left:79px;top:12px;width:1px;height:80px;background:var(--green)}
  .headline{left:88px;top:22px;font-family:'Bebas Neue',sans-serif;font-size:12.5px;line-height:14px;font-weight:400;color:var(--white)}
  .headline strong{display:block;font-weight:400;color:var(--green);font-size:26px;line-height:24px;margin-top:1px}
  .welcome{left:18px;top:106px;font-size:8px;line-height:10px;font-weight:700;color:var(--green);letter-spacing:.2px}
  .perks{left:18px;top:119px;width:170px;list-style:none}
  .perks li{position:relative;padding-left:10px;font-size:7px;line-height:9.6px}
  .perks li::before{content:"";position:absolute;left:1px;top:3px;width:4px;height:4px;border-radius:50%;background:var(--green)}
  .book{left:17px;top:188px;font-size:22px;line-height:24px;font-weight:400}
  .book-sub{left:18px;top:213px;font-size:13.5px;font-weight:800;color:var(--green);letter-spacing:.2px}
  .phone-btn{left:17px;top:232px;width:23px;height:23px;border-radius:50%;background:var(--green);display:flex;align-items:center;justify-content:center}
  .phone-big{left:45px;top:231px;font-size:18.5px;font-weight:800;line-height:24px}
  .contact{display:flex;align-items:center;gap:4px;font-size:4.6px;line-height:6px}
  .icon-ring{width:15px;height:15px;border-radius:50%;border:1.3px solid var(--green);display:flex;align-items:center;justify-content:center;flex:none}
  .portrait{left:262px;top:22px;width:188px;height:283px;border-radius:90px 90px 0 0;background:linear-gradient(180deg,#3a2a24 0%,#b98a72 38%,#e4b79e 55%,#1a2440 80%,#111a33 100%)}
  .badge{left:212px;top:158px;width:112px;height:112px;border-radius:50%;background:linear-gradient(100deg,var(--silver-2),var(--silver-1) 30%,#c9ccd1 55%,var(--silver-1) 75%,var(--silver-2));border:3px solid #e9eaec;box-shadow:0 2px 6px rgba(0,0,0,.3);color:var(--ink);text-align:center;padding-top:30px}
  .badge .b1{font-size:13.5px;font-weight:800;line-height:14px}
  .badge .b2{font-size:8.5px;font-weight:500;line-height:12px}
  .badge .b3{font-size:20px;font-weight:800;line-height:20px;border-bottom:1px solid var(--ink);display:inline-block}
  .doctor-tag{left:353px;top:271px;width:97px;height:22px;border-radius:11px 0 0 11px;background:var(--green);color:var(--ink);font-size:6px;font-weight:600;display:flex;align-items:center;padding-left:8px;white-space:nowrap}

  /* back */
  .tag{left:0;top:15px;width:170px;height:22px;border-radius:0 11px 11px 0;background:var(--green);font-size:10.5px;line-height:22px;padding-left:13px}
  .tag b{font-weight:600}
  .tag span{color:var(--navy)}
  .lead{left:22px;top:54px;width:180px;font-size:7.3px;line-height:9px;font-style:italic}
  .services{left:12px;top:97px;list-style:none}
  .services li{display:flex;align-items:center;gap:5px;height:16px;font-size:8.2px;font-style:italic;line-height:8px;text-transform:uppercase}
  .services li.two{height:24px}
  .dot{width:14px;height:14px;border-radius:50%;background:radial-gradient(circle at 35% 35%,var(--silver-1),var(--silver-2));flex:none;border:1px solid #dfe2e6}
  .call{left:13px;top:248px;font-size:15px;line-height:20px}
  .call-btn{left:73px;top:243px;width:31px;height:31px;border-radius:50%;background:radial-gradient(circle at 35% 35%,var(--silver-1),var(--silver-2));display:flex;align-items:center;justify-content:center}
  .call-num{left:113px;top:248px;font-size:15px;line-height:20px}
  .refer{left:293px;top:20px;width:80px;color:var(--ink)}
  .refer h2{font-size:8.5px;line-height:10px;font-weight:700;color:var(--green)}
  .refer p{font-size:6.2px;line-height:8px;margin-top:3px}
  .refer .refer-mail{font-size:4.6px;line-height:6px;font-weight:600;margin-top:4px;word-break:break-all}
  .stamp{left:380px;top:20px;width:56px;height:59px;border:1px solid #222}
  .addr-line{left:293px;width:143px;height:1px;background:#333}
  .brand-back{left:386px;top:263px;width:52px;font-size:7px;line-height:8.5px;font-weight:500;color:var(--ink)}
</style>
</head>
<body>

<section class="card card--front" aria-label="Postcard front">
  <svg class="shape" viewBox="0 0 450 305" aria-hidden="true">
    <defs>
      <linearGradient id="frontGrad" x1="0" y1="0" x2="1" y2="0.3">
        <stop offset="0" stop-color="#0d3c86"/>
        <stop offset=".55" stop-color="#13658f"/>
        <stop offset="1" stop-color="#14a088"/>
      </linearGradient>
    </defs>
    <path d="M0,0 H272 C216,40 196,130 222,210 C238,260 272,290 322,305 H0Z" fill="var(--mint)"/>
    <path d="M0,0 H258 C204,40 184,130 208,210 C224,260 258,290 306,305 H0Z" fill="var(--green)"/>
    <path d="M0,0 H246 C192,40 172,130 196,210 C212,260 246,290 292,305 H0Z" fill="url(#frontGrad)"/>
  </svg>

  <div class="abs portrait" role="img" aria-label="Portrait photo of Dr. Malvina Okoruwe, MD, smiling, in a dark blue jacket"></div>

  <div class="abs brand">Harborline Family Clinic</div>
  <div class="abs divider"></div>
  <h1 class="abs headline">Experience<br>Individualized Care<br>With a focus on your<strong>Well-Being.</strong></h1>

  <div class="abs welcome">NOW ACCEPTING NEW PATIENTS</div>
  <ul class="abs perks">
    <li>Free consultation – easy to schedule</li>
    <li>Primary, preventive &amp; urgent care</li>
    <li>Traditional + functional medicine</li>
    <li>24-hour direct access to your doctor</li>
    <li>Cutting-edge, individualized plans</li>
  </ul>

  <div class="abs book">BOOK YOUR</div>
  <div class="abs book-sub">FREE CONSULTATION</div>
  <div class="abs phone-btn"><svg width="12" height="12" viewBox="0 0 24 24" aria-hidden="true"><path d="M6.6 10.8a15 15 0 0 0 6.6 6.6l2.2-2.2c.3-.3.7-.4 1-.2 1.1.4 2.3.6 3.6.6.6 0 1 .4 1 1V20c0 .6-.4 1-1 1A17 17 0 0 1 3 4c0-.6.4-1 1-1h3.5c.6 0 1 .4 1 1 0 1.2.2 2.4.6 3.6.1.3 0 .7-.2 1z" fill="#fff"/></svg></div>
  <div class="abs phone-big">727-482-3095</div>

  <div class="abs contact" style="left:18px;top:275px">
    <span class="icon-ring"><svg width="8" height="8" viewBox="0 0 24 24" aria-hidden="true"><circle cx="12" cy="12" r="10" fill="none" stroke="#fff" stroke-width="2"/><path d="M2 12h20M12 2c3 3 3 17 0 20M12 2c-3 3-3 17 0 20" fill="none" stroke="#fff" stroke-width="1.6"/></svg></span>
    <span>WWW.HARBORLINEFAMILYCLINIC.NET<br>OFFICE@HARBORLINEFAMILYCLINIC.ORG</span>
  </div>
  <div class="abs contact" style="left:150px;top:275px">
    <span class="icon-ring"><svg width="8" height="8" viewBox="0 0 24 24" aria-hidden="true"><path d="M12 2a7 7 0 0 0-7 7c0 5 7 13 7 13s7-8 7-13a7 7 0 0 0-7-7z" fill="none" stroke="#fff" stroke-width="2"/><circle cx="12" cy="9" r="2.5" fill="#fff"/></svg></span>
    <span>4187 WRENFIELD AVE, SUITE 214<br>CLEARWATER, FL 33759</span>
  </div>

  <div class="abs badge">
    <div class="b1">SCHEDULE</div>
    <div class="b2">YOUR FIRST VISIT</div>
    <div class="b3">TODAY</div>
  </div>
  <div class="abs doctor-tag">DR. MALVINA OKORUWE, MD</div>
</section>

<section class="card card--back" aria-label="Postcard back">
  <svg class="shape" viewBox="0 0 450 305" aria-hidden="true">
    <defs>
      <linearGradient id="backGrad" x1="0" y1="0" x2="1" y2="0.6">
        <stop offset="0" stop-color="#0d3c86"/>
        <stop offset=".5" stop-color="#14739a"/>
        <stop offset="1" stop-color="#3cc47c"/>
      </linearGradient>
      <radialGradient id="staffGlow" cx=".5" cy=".6" r=".5">
        <stop offset="0" stop-color="#e6d2c0" stop-opacity=".22"/>
        <stop offset="1" stop-color="#e6d2c0" stop-opacity="0"/>
      </radialGradient>
      <clipPath id="backPanel">
        <path d="M0,0 H208 C262,60 290,170 250,240 C235,270 215,290 199,305 H0Z"/>
      </clipPath>
    </defs>
    <path d="M0,0 H226 C284,60 314,170 272,240 C256,270 236,290 218,305 H0Z" fill="var(--mint)"/>
    <path d="M0,0 H216 C272,60 302,170 261,240 C246,270 226,290 208,305 H0Z" fill="var(--green)"/>
    <path d="M0,0 H208 C262,60 290,170 250,240 C235,270 215,290 199,305 H0Z" fill="url(#backGrad)"/>
    <g clip-path="url(#backPanel)">
      <rect x="140" y="150" width="120" height="90" fill="url(#staffGlow)" role="img" aria-label="Faded photo of smiling clinic staff"/>
      <rect x="0" y="236" width="300" height="69" fill="rgba(10,40,100,.35)"/>
    </g>
  </svg>

  <div class="abs tag"><b>PERSONALIZED</b> <span>TREATMENT</span></div>
  <p class="abs lead">No one-size-fits-all plans – your care may include:</p>

  <ul class="abs services">
    <li><span class="dot"></span>Genomics and Pharmacogenomics</li>
    <li><span class="dot"></span>Advanced Heart Disease Screening &amp; Evaluation</li>
    <li><span class="dot"></span>Advanced Nutritional Status Evaluation</li>
    <li><span class="dot"></span>Pulsed Electromagnetic Field Therapy</li>
    <li><span class="dot"></span>Bioidentical Hormone Replacement Therapy</li>
    <li class="two"><span class="dot"></span>Advanced Multi-Cancer Screening Veltrion<br>Panorama Test</li>
    <li><span class="dot"></span>Prescription Exercise</li>
    <li><span class="dot"></span>Personalized Vitamins</li>
  </ul>

  <div class="abs call">CALL US</div>
  <div class="abs call-btn"><svg width="14" height="14" viewBox="0 0 24 24" aria-hidden="true"><path d="M6.6 10.8a15 15 0 0 0 6.6 6.6l2.2-2.2c.3-.3.7-.4 1-.2 1.1.4 2.3.6 3.6.6.6 0 1 .4 1 1V20c0 .6-.4 1-1 1A17 17 0 0 1 3 4c0-.6.4-1 1-1h3.5c.6 0 1 .4 1 1 0 1.2.2 2.4.6 3.6.1.3 0 .7-.2 1z" fill="var(--navy)"/></svg></div>
  <div class="abs call-num">(727)482-3095</div>

  <div class="abs contact" style="left:13px;top:277px">
    <span class="icon-ring" style="width:13px;height:13px"><svg width="7" height="7" viewBox="0 0 24 24" aria-hidden="true"><circle cx="12" cy="12" r="10" fill="none" stroke="#fff" stroke-width="2"/><path d="M2 12h20M12 2c3 3 3 17 0 20M12 2c-3 3-3 17 0 20" fill="none" stroke="#fff" stroke-width="1.6"/></svg></span>
    <span style="font-size:4.3px">WWW.HARBORLINEFAMILYCLINIC.NET</span>
  </div>
  <div class="abs contact" style="left:108px;top:277px">
    <span class="icon-ring" style="width:13px;height:13px"><svg width="7" height="7" viewBox="0 0 24 24" aria-hidden="true"><path d="M12 2a7 7 0 0 0-7 7c0 5 7 13 7 13s7-8 7-13a7 7 0 0 0-7-7z" fill="none" stroke="#fff" stroke-width="2"/><circle cx="12" cy="9" r="2.5" fill="#fff"/></svg></span>
    <span style="font-size:4.3px;line-height:5px">4187 WRENFIELD AVE, SUITE 214<br>CLEARWATER, FL 33759</span>
  </div>

  <div class="abs refer">
    <h2>REFER A FRIEND</h2>
    <p>Share the same level of care with family &amp; friends</p>
    <p class="refer-mail">OFFICE@HARBORLINEFAMILYCLINIC.ORG</p>
  </div>
  <div class="abs stamp"></div>
  <div class="abs addr-line" style="top:157px"></div>
  <div class="abs addr-line" style="top:179px"></div>
  <div class="abs addr-line" style="top:201px"></div>
  <div class="abs addr-line" style="top:224px"></div>

  <div class="abs brand-back">Harborline Family Clinic</div>
</section>

</body>
</html>
```